Vitamin C Serum Packaging and Label re-design

Redesign exciting packaging and label re-design
naturals
Vitamin C 20%
E & Hyaluronic Acid
PROFESSIONAL Facial Serum
1 fl oz / 30ml
Ingredients: Aqua,Glycerin,Propylene Glycol,Sodium Hyaluronate,Niacinamide,Carbomer,Triethanolamine,Betaglucan,Ascorbic Acid, Ethylhexylglycerin,Caprylyl Glycol,Propanediol,Phenylpropanol.
72% Organic
FOR EXTERNAL USE ONLY
MADE IN CHINA
Product Description
Vitamin C serum has the Anti Aging power of Vitamin C + E + Amino + Hyaluronic Acid. Bold Lantern Skin Care gives you the highest quality Vitamin C Serum on the market with 98% Natural & 72% Organic ingredients.
Our 20% Vitamin C Serum Provides Your Skin With The Following Benefits:
1- Stimulates the production of collagen which makes your skin more vibrant, firm and youthful.
2- Contains Antioxidants that will greatly reduce skin damage caused by the sun, pollution and impurities in the air.
3- Enhances your skins rate of exfoliation for a smoother, brighter and more radiant complexion.
4- Greatly Diminishes the appearance of fine lines and wrinkles.
5- Has a high percentage of Hyaluronic Acid which deeply moisturizes the skin to reduce skin problems that occur due to age.
How to use
Dispense 2-3 drops into the palm of your hand and then apply to your face and neck. During the day, finish with a moisturizer with SPF 30 or greater. Can be applied under the eye area, avoiding the eye itself.
NON-IRRITATING, FRAGRANCE FREE, AND NEVER ANIMAL TESTED
Ingredients: Aqua, Ascorbic Acid (Vitamin C), Glycerin (Humectant), Sodium Hyaluronate (Hyaluronic Acid), Propylene Glycol (Humectant), Vitamin E, Niacinamide (Vitamin B3), Carbomer, Propanediol, Ethylhexylglycerin, Caprylyl Glycol, Phenylpropanol, Triethanolamine.
Store at 20- 75° C (68-77° F) Keep out of Direct Sunlight.
USA Company, Veteran owned and operated. 5% of sales will be donated to a nonprofit Veterans organization.
BoldLanternSkinCare.com
Target Market(s)
female and males for skin care product
Industry/Entity Type
Skin Care
Requirements
Must have
- Exciting logo.
Nice to have
- Army Green, Black, Gray colors to make it Sex Neutral. I want a fell of luxury and sophisticated packaging.

```html
<!DOCTYPE html>
<html lang="en">
<head>
<meta charset="utf-8">
<title>Bold Lantern Skin Care – Vitamin C Serum Box Dieline</title>
<link rel="stylesheet" href="https://fonts.googleapis.com/css2?family=Arimo:wght@400;700&family=Lato:wght@400;700&family=Signika:wght@600&display=swap">
<style>
  :root {
    --panel: #e6e7e8;
    --paper: #ffffff;
    --ink: #231f20;
    --ink-soft: #3d3b3c;
    --army: #4b5b36;
    --orange: #f58634;
    --sage: #c8c9bf;
  }
  * { margin: 0; padding: 0; box-sizing: border-box; }
  html, body { width: 1200px; height: 1200px; overflow: hidden; background: var(--paper); }
  .dieline { position: relative; width: 1200px; height: 1200px; font-family: "Arimo", Arial, sans-serif; color: var(--ink); }
  .dieline-shapes { position: absolute; inset: 0; }

  .copy { position: absolute; font-size: 11.9px; line-height: 13.45px; }
  .copy p { margin-bottom: 13.45px; text-align: justify; }
  .copy p.ragged { text-align: left; }
  .copy strong { font-weight: 700; }
  .side-left { left: 119px; top: 347px; width: 182px; }
  .side-right { left: 548px; top: 347px; width: 182px; }
  .claims { font-weight: 700; letter-spacing: 0.3px; }

  .brand-name {
    position: absolute; text-align: center;
    font-family: "Lato", Arial, sans-serif; font-weight: 700;
    color: var(--ink-soft); letter-spacing: 1.5px; text-transform: uppercase;
  }
  .brand-mark { position: absolute; border-radius: 50%; background: var(--army); }

  .front { position: absolute; left: 317px; top: 328px; width: 216px; height: 564px; text-align: center; }
  .front .brand-mark { left: 98px; top: 38px; width: 20px; height: 20px; }
  .front .brand-name { left: 0; right: 0; top: 80px; font-size: 17px; line-height: 21px; }
  .front .tagline { position: absolute; left: 0; right: 0; top: 125px; font-family: "Lato", sans-serif; font-size: 9.4px; letter-spacing: 0.2px; }
  .front .natural { position: absolute; left: 0; right: 0; top: 165px; font-family: "Signika", sans-serif; font-weight: 600; font-size: 16px; line-height: 17.5px; color: var(--army); letter-spacing: 0.5px; }
  .front .vitamin-c { position: absolute; left: 30px; top: 240px; width: 160px; height: 160px; }
  .front .strength { position: absolute; left: 155px; top: 323px; font-family: "Signika", sans-serif; font-weight: 600; font-style: italic; font-size: 20px; color: var(--army); }
  .pill {
    position: absolute; left: 8px; top: 469px; width: 199px; height: 28px; border-radius: 14px;
    background: var(--army); color: #fff; font-family: "Signika", sans-serif; font-weight: 600;
    font-size: 9.8px; line-height: 28px; letter-spacing: 0.2px;
  }
  .front .format { position: absolute; left: 0; right: 0; top: 513px; font-family: "Lato", sans-serif; font-size: 9.8px; line-height: 13.5px; }

  .back { position: absolute; left: 746px; top: 328px; width: 215px; height: 846px; }
  .back .decor { position: absolute; left: 7px; top: 10px; width: 201px; height: 540px; }
  .back .brand-mark { left: 98px; top: 250px; width: 20px; height: 20px; }
  .back .brand-name { left: 0; right: 0; top: 292px; font-size: 17px; line-height: 21px; }

  .label { position: absolute; left: 758px; top: 113px; width: 359px; height: 154px; background: var(--panel); }
  .label .brand-mark { left: 84px; top: 14px; width: 12px; height: 12px; }
  .label .brand-name { left: 10px; width: 160px; top: 34px; font-size: 10px; line-height: 12px; }
  .label .tagline { position: absolute; left: 10px; width: 160px; top: 64px; text-align: center; font-family: "Lato", sans-serif; font-size: 5.6px; }
  .label .natural { position: absolute; left: 49px; top: 83px; font-family: "Signika", sans-serif; font-weight: 600; font-size: 8.4px; line-height: 8.6px; color: var(--army); text-align: right; }
  .label .vitamin-c { position: absolute; left: 84px; top: 79px; width: 30px; height: 30px; }
  .label .strength { position: absolute; left: 115px; top: 95px; font-family: "Signika", sans-serif; font-weight: 600; font-style: italic; font-size: 6.6px; color: var(--army); }
  .label .pill { left: 15px; top: 114px; width: 150px; height: 16px; line-height: 16px; font-size: 5.7px; border-radius: 8px; }
  .label .format { position: absolute; left: 10px; width: 160px; top: 133px; text-align: center; font-family: "Lato", sans-serif; font-size: 5.6px; line-height: 7px; }
  .label-copy { position: absolute; left: 195px; top: 5px; width: 149px; font-size: 5.4px; line-height: 6.7px; }
  .label-copy p { margin-bottom: 4px; text-align: justify; }
  .label-copy .web { position: absolute; top: 140px; left: 0; }
</style>
</head>
<body>
<main class="dieline">
  <svg class="dieline-shapes" viewBox="0 0 1920 1920" width="1200" height="1200" aria-hidden="true">
    <g fill="var(--panel)">
      <path d="M501,525 L507,500 L507,115 Q507,75 547,75 L812,75 Q852,75 852,115 L852,500 L858,525 Z"/>
      <path d="M223,300 L501,300 L501,500 L507,525 L507,1428 L501,1455 L501,1652 L223,1652 L223,1493 L166,1428 L67,1388 L67,565 L166,525 L223,460 Z"/>
      <rect x="507" y="525" width="345" height="903"/>
      <path d="M858,300 L1136,300 L1136,460 L1193,525 L1193,1428 L1136,1493 L1136,1652 L858,1652 L858,1455 L852,1428 L852,525 L858,500 Z"/>
      <path d="M1193,525 L1538,525 L1538,1838 Q1538,1878 1498,1878 L1233,1878 Q1193,1878 1193,1838 Z"/>
    </g>
    <circle cx="680" cy="355" r="125" fill="var(--sage)" opacity="0.45" role="img" aria-label="Faint brand emblem area on tuck flap"/>
  </svg>

  <section class="copy side-left">
    <p class="ragged">MADE IN CHINA</p>
    <p><strong>Product Description</strong><br>Vitamin C serum has the Anti Aging power of Vitamin C + E + Amino + Hyaluronic Acid. Bold Lantern Skin Care gives you the highest quality Vitamin C Serum on the market with 98% Natural &amp; 72% Organic ingredients.</p>
    <p>Our 20% Vitamin C Serum Provides Your Skin With The Following Benefits:</p>
    <p>1- Stimulates the production of collagen which makes your skin more vibrant, firm and youthful.</p>
    <p>2- Contains Antioxidants that will greatly reduce skin damage caused by the sun, pollution and impurities in the air.</p>
    <p>3- Enhances your skins rate of exfoliation for a smoother, brighter and more radiant complexion.</p>
    <p>4- Greatly Diminishes the appearance of fine lines and wrinkles.</p>
    <p>5- Has a high percentage of Hyaluronic Acid which deeply moisturizes the skin to reduce skin problems that occur due to age.</p>
  </section>

  <section class="front">
    <span class="brand-mark"></span>
    <h1 class="brand-name">Bold Lantern<br>Skin Care</h1>
    <p class="tagline">PROFESIONAL DAY AND NIGHT SERUM</p>
    <p class="natural">Natural<br>Vitamin</p>
    <svg class="vitamin-c" viewBox="0 0 160 160" aria-hidden="true">
      <path d="M132.5,49.5 A60,60 0 1 0 132.5,110.5" fill="none" stroke="var(--orange)" stroke-width="38"/>
    </svg>
    <span class="strength">20%</span>
    <div class="pill">With Vitamin E &amp; Hyaluronic Acid</div>
    <p class="format">PROFESSIONAL FACIAL SERUM<br>1 fl oz / 30ml</p>
  </section>

  <section class="copy side-right">
    <p class="ragged"><strong>How to use :</strong><br></p>
    <p style="margin-top:-13.45px">Dispense 2-3 drops into the palm of your hand and then apply to your face and neck. During the day, finish with a moisturizer with SPF 30 or greater. Can be applied under the eye area, avoiding the eye itself.</p>
    <p class="claims">NON-IRRITATING, FRAGRANCE FREE, AND NEVER ANIMAL TESTED</p>
    <p><strong>Ingredients:</strong> Aqua, Ascorbic Acid (Vitamin C), Glycerin (Humectant), Sodium Hyaluronate (Hyaluronic Acid), Propylene Glycol (Humectant), Vitamin E, Niacinamide (Vitamin B3), Carbomer, Propanediol, Ethylhexylglycerin, Caprylyl Glycol, Phenylpropanol, Triethanolamine.</p>
    <p>Store at 20- 75° C (68-77° F) Keep out of Direct Sunlight.</p>
    <p>USA Company, Veteran owned and operated. 5% of sales will be donated to a nonprofit Veterans organization.</p>
    <p class="ragged">Brookvale <strong>FL 33990</strong></p>
  </section>

  <section class="back">
    <svg class="decor" viewBox="0 0 201 540" role="img" aria-label="Large faint brand emblem decoration">
      <circle cx="100.5" cy="270" r="100" fill="var(--sage)" opacity="0.7"/>
    </svg>
    <span class="brand-mark"></span>
    <h2 class="brand-name">Bold Lantern<br>Skin Care</h2>
  </section>

  <section class="label">
    <span class="brand-mark"></span>
    <h2 class="brand-name">Bold Lantern<br>Skin Care</h2>
    <p class="tagline">PROFESIONAL DAY AND NIGHT SERUM</p>
    <p class="natural">Natural<br>Vitamin</p>
    <svg class="vitamin-c" viewBox="0 0 160 160" aria-hidden="true">
      <path d="M132.5,49.5 A60,60 0 1 0 132.5,110.5" fill="none" stroke="var(--orange)" stroke-width="38"/>
    </svg>
    <span class="strength">20%</span>
    <div class="pill">With Vitamin E &amp; Hyaluronic Acid</div>
    <p class="format">PROFESSIONAL FACIAL SERUM<br>1 fl oz / 30ml</p>
    <div class="label-copy">
      <p><strong>How to use :</strong><br>Dispense 2-3 drops into the palm of your hand and then apply to your face and neck. During the day, finish with a moisturizer with SPF 30 or greater. Can be applied under the eye area, avoiding the eye itself.</p>
      <p><strong>NON-IRRITATING, FRAGRANCE FREE, AND NEVER ANIMAL TESTED</strong></p>
      <p><strong>Ingredients:</strong> Aqua, Ascorbic Acid (Vitamin C), Glycerin (Humectant), Sodium Hyaluronate (Hyaluronic Acid), Propylene Glycol (Humectant), Vitamin E, Niacinamide (Vitamin B3), Carbomer, Propanediol, Ethylhexylglycerin, Caprylyl Glycol, Phenylpropanol, Triethanolamine.</p>
      <p>Store at 20- 75° C (68-77° F) Keep out of Direct Sunlight.</p>
      <p>USA Company, Veteran owned and operated. 5% of sales will be donated to a nonprofit Veterans.</p>
      <span class="web">BoldLanternSkinCare.com</span>
    </div>
  </section>
</main>
</body>
</html>
```